Workplace Safety Consultancy Business needs business card design

We need a business card for a new business providing workplace health and safety consulting called 'Worksure Guard'. We will be providing small to medium sized businesses assistance with OH&S and HR matters to ensure that their employees and the public are safe in the workplace and that they are meeting their legislative requirements. Would like to see the words 'Clear Steps To Safer Worksites' on the card. Personal details on the back. It needs to be clean, smart and professional (no fluff). Would like to see a simple logo if possible as well. Have been looking at orange and black, but open to other ideas.
Updates
Thank you to those to have created designs for us so far! We are really impressed with the impact of the black and orange having now seen it. Would be great if any further designs used those colours. Cheers.

Thank you to everyone that submitted a design. Your work is of the highest quality and we had a hard decision deciding. Sorry if we didn't choose your design, but it just came down to the one that stood out to us personally. Cheers.

Target Market(s)
Small-Medium business owners in Queensland, Australia. Age 25-60 male and female. Initially targeting those in the trade type industries
Industry/Entity Type
Health
Look and feel
Each slider illustrates characteristics of the customer's brand and the style your logo design should communicate.

```html
<!DOCTYPE html>
<html lang="en">
<head>
<meta charset="utf-8">
<title>Worksure Guard business card</title>
<link rel="stylesheet" href="https://fonts.googleapis.com/css2?family=Cabin:wght@400;600;700&display=swap">
<style>
  :root {
    --page: #ffffff;
    --ink-black: #1b1b1b;
    --ink-black-edge: #2a2a2a;
    --orange: #f6a400;
    --orange-light: #f9c13d;
    --orange-band: rgba(255, 214, 110, 0.55);
    --white: #ffffff;
    --text-dark: #3a2a05;
  }
  * { margin: 0; padding: 0; box-sizing: border-box; }
  html, body {
    width: 1200px; height: 415px; overflow: hidden;
    background: var(--page);
    font-family: "Cabin", "Gill Sans", sans-serif;
  }
  .canvas { position: relative; width: 1200px; height: 415px; }

  .card {
    position: absolute; top: 24px;
    width: 560px; height: 360px;
    border-radius: 14px; overflow: hidden;
  }

  /* Back: personal details */
  .card--back { left: 32px; background: var(--ink-black); box-shadow: inset 0 0 0 1px var(--ink-black-edge); }
  .card--back .brand { position: absolute; left: 42px; top: 56px; }
  .details-band {
    position: absolute; left: 0; right: 0; bottom: 0; height: 118px;
    background: linear-gradient(90deg, var(--orange) 0%, var(--orange-light) 100%);
  }
  .person { position: absolute; left: 42px; top: 34px; color: var(--text-dark); }
  .person__name { font-size: 17px; font-weight: 400; }
  .person__role { font-size: 15px; font-style: italic; margin-top: 4px; }
  .contacts {
    position: absolute; left: 250px; top: 22px;
    list-style: none; color: var(--white); font-size: 14px;
  }
  .contacts li { display: flex; align-items: center; height: 22px; }
  .contacts .label { width: 30px; font-size: 11px; font-weight: 700; color: var(--white); opacity: 0.9; }

  /* Front: brand */
  .card--front { left: 618px; background: var(--orange); }
  .band { position: absolute; background: var(--orange-band); }
  .band--vertical { left: 98px; top: 0; bottom: 0; width: 82px; }
  .band--horizontal { left: 0; right: 0; top: 118px; height: 110px; }
  .card--front .brand { position: absolute; left: 116px; top: 150px; }

  /* Brand lockup */
  .brand__row { display: flex; align-items: center; gap: 10px; }
  .brand__mark { width: 24px; height: 24px; background: var(--ink-black); flex: none; }
  .card--back .brand__mark { background: var(--orange); }
  .brand__name {
    font-size: 26px; font-weight: 700; letter-spacing: 0.5px;
    text-transform: uppercase; color: var(--white); line-height: 1;
  }
  .brand__tagline {
    margin: 5px 0 0 34px;
    font-size: 10px; font-weight: 600; letter-spacing: 0.6px;
    text-transform: uppercase; color: var(--white);
  }
</style>
</head>
<body>
<main class="canvas">

  <section class="card card--back" aria-label="Card back with personal details">
    <div class="brand">
      <div class="brand__row">
        <span class="brand__mark" aria-hidden="true"></span>
        <span class="brand__name">Worksure Guard</span>
      </div>
      <p class="brand__tagline">Clear steps to safer worksites</p>
    </div>
    <div class="details-band">
      <div class="person">
        <p class="person__name">Daniel Corrigan</p>
        <p class="person__role">Managing Director</p>
      </div>
      <ul class="contacts">
        <li><span class="label">m</span>0400 318 526</li>
        <li><span class="label">e</span>daniel@worksureguard.com.au</li>
        <li><span class="label">w</span>worksureguard.com.au</li>
      </ul>
    </div>
  </section>

  <section class="card card--front" aria-label="Card front with brand name">
    <span class="band band--vertical" aria-hidden="true"></span>
    <span class="band band--horizontal" aria-hidden="true"></span>
    <div class="brand">
      <div class="brand__row">
        <span class="brand__mark" aria-hidden="true"></span>
        <span class="brand__name">Worksure Guard</span>
      </div>
      <p class="brand__tagline">Clear steps to safer worksites</p>
    </div>
  </section>

</main>
</body>
</html>
```